Process Flow Chart for Real Estate Agency

We need a visual flow chart of the process of selling a home for our Real Estate Agency. This visual will be provided to all new staff to explain the process and also to potential clients to explain how detailed the process is. It needs to show each step as detailed in the attached word doc and use icons and arrows to show the direction of flow.

Target Market(s)

Staff & Potential Clients

Industry/Entity Type

Real Estate

Font styles to use
Sans Serif

Colors

Designer to choose colors to be used in the design.

Requirements
Must have
• Easy to read, lots of icons, colour coded with Agent in one colour, Admin in another (some tasks are either/or so not sure what to colour those ones.)
Nice to have
• Include one of the two attached logos

```html
<!DOCTYPE html>
<html lang="en">
<head>
<meta charset="utf-8">
<title>Listing Process Flow – Hartwell Partners</title>
<link href="https://fonts.googleapis.com/css2?family=Roboto:wght@400;700;900&display=swap" rel="stylesheet">
<style>
  :root{
    --brand-blue:#1b8ad6;
    --keyword-blue:#1e86d0;
    --ink:#333a40;
    --paper:#ffffff;
  }
  html,body{margin:0;padding:0;width:927px;height:1200px;overflow:hidden;background:var(--paper);}
  .flow-chart{display:block;width:927px;height:1200px;font-family:"Roboto",Arial,sans-serif;}
  .step-text{fill:var(--ink);font-size:18px;font-weight:400;}
  .step-text.small{font-size:16px;}
  .kw{fill:var(--keyword-blue);font-weight:900;letter-spacing:.6px;}
  .flow-line{fill:none;stroke:var(--brand-blue);stroke-width:2;}
  .arrow{fill:var(--brand-blue);}
  .node{fill:var(--paper);stroke:var(--brand-blue);stroke-width:2.5;}
  .glyph{color:var(--brand-blue);}
  .banner{fill:var(--brand-blue);}
  .banner-label{fill:#fff;font-size:36px;font-weight:900;letter-spacing:1px;}
  .brand-name{fill:var(--ink);font-size:22px;font-weight:700;}
  .brand-dot{fill:var(--brand-blue);}
</style>
</head>
<body>
<svg class="flow-chart" viewBox="0 0 1160 1500" xmlns="http://www.w3.org/2000/svg" role="img" aria-label="Listing process flow chart">
  <defs>
    <path id="ar" d="M-8,-10 L7,0 L-8,10 L-4,0Z"/>
    <symbol id="i-phone" viewBox="0 0 24 24"><path d="M6 3 L9 3 L10.5 8 L8.5 9.5 Q10 13.5 14.5 15.5 L16 13.5 L21 15 L21 18 Q20 21 17 21 Q4 19 3 6 Q3 3 6 3Z" fill="currentColor"/></symbol>
    <symbol id="i-people" viewBox="0 0 24 24" fill="none" stroke="currentColor" stroke-width="1.8"><circle cx="12" cy="5" r="2.5"/><path d="M8 14 V10 H16 V14"/><circle cx="5" cy="11" r="2"/><circle cx="19" cy="11" r="2"/><path d="M2 20 V17 H8 V20 M16 20 V17 H22 V20 M12 14 V21"/></symbol>
    <symbol id="i-card" viewBox="0 0 24 24"><rect x="2" y="5" width="20" height="14" rx="2" fill="currentColor"/><circle cx="8" cy="11" r="2.3" fill="#fff"/><path d="M5 16 Q8 12 11 16Z" fill="#fff"/><rect x="13" y="9" width="6" height="1.6" fill="#fff"/><rect x="13" y="12" width="6" height="1.6" fill="#fff"/><rect x="13" y="15" width="4" height="1.6" fill="#fff"/></symbol>
    <symbol id="i-cal" viewBox="0 0 24 24" fill="none" stroke="currentColor" stroke-width="1.8"><rect x="3" y="5" width="18" height="16" rx="2"/><path d="M3 9 H21 M8 3 V7 M16 3 V7"/><path d="M7 13h2M11 13h2M15 13h2M7 17h2M11 17h2" stroke-width="2"/></symbol>
    <symbol id="i-sms" viewBox="0 0 24 24" fill="none" stroke="currentColor" stroke-width="1.8"><rect x="4" y="2" width="12" height="20" rx="2"/><path d="M9 19h2"/><rect x="10" y="6" width="12" height="8" rx="2" fill="#fff"/><path d="M13 10h.1M16 10h.1M19 10h.1" stroke-width="2.5" stroke-linecap="round"/></symbol>
    <symbol id="i-order" viewBox="0 0 24 24" fill="none" stroke="currentColor" stroke-width="1.8"><rect x="6" y="3" width="13" height="16" rx="1" transform="rotate(12 12 12)"/><path d="M9 8h7M9 11h7M9 14h5" transform="rotate(12 12 12)"/><path d="M3 21 L8 17"/></symbol>
    <symbol id="i-list" viewBox="0 0 24 24" fill="none" stroke="currentColor" stroke-width="1.8"><rect x="4" y="3" width="16" height="18" rx="2"/><path d="M7 8h1M7 12h1M7 16h1M10 8h7M10 12h7M10 16h7"/></symbol>
    <symbol id="i-clip" viewBox="0 0 24 24" fill="none" stroke="currentColor" stroke-width="1.8"><rect x="4" y="4" width="14" height="18" rx="2"/><rect x="8" y="2" width="6" height="4" rx="1"/><path d="M7 10h8M7 14h5M7 18h4"/><path d="M14 20 L21 11" stroke-width="2.2"/></symbol>
    <symbol id="i-grid" viewBox="0 0 24 24" fill="none" stroke="currentColor" stroke-width="1.6"><rect x="3" y="4" width="18" height="16" rx="2"/><path d="M3 8 H21 M7 11h2M11 11h2M15 11h2M7 14h2M11 14h2M7 17h2M11 17h2"/><circle cx="17" cy="16" r="2.5"/></symbol>
    <symbol id="i-chart" viewBox="0 0 24 24" fill="none" stroke="currentColor" stroke-width="1.8"><rect x="4" y="3" width="16" height="18" rx="2"/><path d="M8 17V13M12 17V10M16 17V8"/><path d="M7 10 L11 7 L14 9 L17 5"/></symbol>
    <symbol id="i-book" viewBox="0 0 24 24" fill="none" stroke="currentColor" stroke-width="1.8"><rect x="5" y="3" width="13" height="17" rx="1"/><path d="M8 7h7M8 10h7M8 13h4"/><path d="M12 21 L20 14 L22 16 L14 22Z"/></symbol>
    <symbol id="i-target" viewBox="0 0 24 24" fill="none" stroke="currentColor" stroke-width="1.8"><circle cx="12" cy="12" r="9"/><circle cx="12" cy="12" r="5"/><circle cx="12" cy="12" r="1.5" fill="currentColor"/><path d="M12 3V7M12 17V21M3 12H7M17 12H21"/></symbol>
    <symbol id="i-tick" viewBox="0 0 24 24" fill="none" stroke="currentColor" stroke-width="2"><path d="M21 12 A9 9 0 1 1 15 3.5" stroke-dasharray="3 2"/><path d="M7 12 L11 16 L20 6"/></symbol>
    <symbol id="i-award" viewBox="0 0 24 24" fill="none" stroke="currentColor" stroke-width="1.8"><circle cx="12" cy="9" r="6.5"/><path d="M9 9 L11 11 L15 7"/><path d="M8 14 L5 21 L8 20 L10 22 L12 16 L14 22 L16 20 L19 21 L16 14"/></symbol>
    <symbol id="i-gift" viewBox="0 0 24 24" fill="none" stroke="currentColor" stroke-width="1.8"><rect x="3" y="8" width="18" height="4"/><rect x="5" y="12" width="14" height="9"/><path d="M12 8V21"/><path d="M12 8 Q7 2 6 6 Q6 8 12 8 Q17 2 18 6 Q18 8 12 8"/></symbol>
    <symbol id="i-hand" viewBox="0 0 24 24"><rect x="9" y="3" width="10" height="8" rx="1" fill="currentColor"/><path d="M3 12 H7 V21 H3Z M7 13 Q12 12 14 14 L19 13 Q21 14 19 16 L12 19 L7 18Z" fill="currentColor"/></symbol>
    <symbol id="i-doc" viewBox="0 0 24 24" fill="none" stroke="currentColor" stroke-width="1.8"><path d="M5 2 H15 L19 6 V22 H5Z"/><path d="M8 9h3M8 13h8M8 16h8M8 19h6"/><path d="M15 8.5 Q13 8 13.5 10 Q16 11 14 12.5 M14.5 7.5V13"/></symbol>
    <symbol id="i-tag" viewBox="0 0 24 24" fill="currentColor"><path d="M13 2 H22 V11 L11 22 L2 13Z"/><circle cx="18" cy="6" r="1.6" fill="#fff"/><text x="9" y="16" font-size="8" font-weight="900" fill="#fff" font-family="Roboto,Arial,sans-serif" transform="rotate(-45 11 13)">$</text></symbol>
    <symbol id="i-mail" viewBox="0 0 24 24"><rect x="2" y="5" width="20" height="14" rx="2" fill="currentColor"/><path d="M3 7 L12 13 L21 7 M3 18 L9 12 M21 18 L15 12" fill="none" stroke="#fff" stroke-width="1.6"/></symbol>
    <symbol id="i-checklist" viewBox="0 0 24 24" fill="none" stroke="currentColor" stroke-width="1.8"><rect x="3" y="3" width="15" height="18" rx="2"/><path d="M6 8 L7.5 9.5 L10 7M6 13 L7.5 14.5 L10 12M12 8h3M12 13h3M6 18h5"/><path d="M14 21 L21 12 L23 14 L16 22Z"/></symbol>
    <symbol id="i-cloud" viewBox="0 0 24 24" fill="none" stroke="currentColor" stroke-width="1.6"><path d="M6 19 Q1 19 2 14 Q3 10 7 11 Q8 5 14 6 Q19 7 19 11 Q23 12 22 16 Q21 19 18 19Z"/><text x="5.5" y="17.5" font-size="6.5" font-weight="700" fill="currentColor" stroke="none" font-family="Roboto,Arial,sans-serif">CRM</text></symbol>
    <symbol id="i-folder" viewBox="0 0 24 24" fill="currentColor"><path d="M2 5 H9 L11 7 H21 V19 H2Z" opacity=".55"/><path d="M2 9 H22 L20 20 H2Z"/></symbol>
    <symbol id="i-network" viewBox="0 0 24 24" fill="none" stroke="currentColor" stroke-width="1.7"><rect x="8" y="2" width="8" height="6" rx="1"/><rect x="2" y="16" width="6" height="6" rx="1"/><rect x="9" y="16" width="6" height="6" rx="1"/><rect x="16" y="16" width="6" height="6" rx="1"/><path d="M12 8V16M5 16V12H19V16"/></symbol>
    <symbol id="i-add" viewBox="0 0 24 24" fill="none" stroke="currentColor" stroke-width="1.8"><rect x="3" y="7" width="14" height="14" rx="1"/><rect x="7" y="3" width="14" height="14" rx="1" fill="#fff"/><path d="M14 7V13M11 10H17"/></symbol>
    <symbol id="i-save" viewBox="0 0 24 24" fill="none" stroke="currentColor" stroke-width="1.8"><path d="M3 3 H18 L21 6 V21 H3Z"/><rect x="7" y="3" width="9" height="6"/><rect x="6" y="13" width="12" height="8"/><path d="M8 16h8M8 18.5h8"/></symbol>
    <symbol id="i-invoice" viewBox="0 0 24 24" fill="none" stroke="currentColor" stroke-width="1.8"><rect x="4" y="2" width="16" height="20" rx="1"/><path d="M7 7h5M7 11h5M7 15h5M7 19h10"/><path d="M17.5 6 Q15 5.5 15 7.5 Q15 9 17 9.5 Q18.5 10 18 12 Q17 13 15 12 M16.5 4.5V13.5"/></symbol>
    <symbol id="i-form" viewBox="0 0 24 24" fill="none" stroke="currentColor" stroke-width="1.8"><rect x="3" y="3" width="18" height="18" rx="1"/><path d="M6 7h12M6 10h3M11 10h7M6 14h3M11 14h7M6 18h12"/></symbol>
    <symbol id="i-gavel" viewBox="0 0 24 24" fill="currentColor"><rect x="7" y="2" width="9" height="6" rx="1" transform="rotate(45 11.5 5)"/><path d="M12 10 L21 19 L19 21 L10 12Z"/><rect x="3" y="19" width="11" height="3" rx="1"/></symbol>
    <symbol id="i-paper" viewBox="0 0 24 24" fill="none" stroke="currentColor" stroke-width="1.7"><path d="M4 2 H14 L18 6 V20 H4Z"/><path d="M7 8h7M7 11h7M7 14h4"/><circle cx="18" cy="18" r="4.5" fill="#fff"/><path d="M16 18 L17.5 19.5 L20 16.5"/></symbol>
    <symbol id="i-box" viewBox="0 0 24 24" fill="currentColor"><path d="M4 8 Q4 4 8 4 H17 Q21 4 21 8 V16 H4Z"/><path d="M12 4 V2 H16 V4" fill="none" stroke="currentColor" stroke-width="1.5"/><rect x="11" y="16" width="3" height="7"/><path d="M8 7 Q6 7 6 9 V14 H10 V9 Q10 7 8 7Z" fill="#fff"/></symbol>
    <symbol id="i-clock" viewBox="0 0 24 24" fill="none" stroke="currentColor" stroke-width="1.8"><circle cx="12" cy="12" r="9.5"/><circle cx="12" cy="12" r="6"/><path d="M12 8 V12 L15 14"/></symbol>
    <symbol id="i-shield" viewBox="0 0 24 24" fill="none" stroke="currentColor" stroke-width="1.8"><path d="M12 2 L20 5 V12 Q20 19 12 22 Q4 19 4 12 V5Z"/><path d="M8 12 L11 15 L16 9"/></symbol>
    <symbol id="i-plan" viewBox="0 0 24 24" fill="none" stroke="currentColor" stroke-width="1.6"><rect x="3" y="3" width="18" height="18"/><path d="M3 10 H10 V3 M10 14 V21 M14 3 V10 H21 M14 14 H21 M10 14 H7"/></symbol>
  </defs>

  <!-- Header -->
  <polygon class="banner" points="0,32 310,32 285,52 310,72 0,72"/>
  <text class="banner-label" x="78" y="66">TASK</text>
  <circle class="brand-dot" cx="920" cy="42" r="14"/>
  <text class="brand-name" x="942" y="50">Hartwell Partners</text>

  <!-- Flow path -->
  <polyline class="flow-line" points="68,117 68,200 1125,200 1125,365 68,365 68,530 1125,530 1125,697 68,697 68,872 1115,872 1115,1013 68,1013 68,1188 1110,1188 1110,1368 68,1368 68,1500"/>

  <!-- Arrows -->
  <g class="arrow">
    <use href="#ar" transform="translate(315,200)"/><use href="#ar" transform="translate(527,200)"/><use href="#ar" transform="translate(720,200)"/><use href="#ar" transform="translate(1015,200)"/>
    <use href="#ar" transform="translate(290,365) rotate(180)"/><use href="#ar" transform="translate(565,365) rotate(180)"/><use href="#ar" transform="translate(868,365) rotate(180)"/><use href="#ar" transform="translate(1070,365) rotate(180)"/>
    <use href="#ar" transform="translate(250,530)"/><use href="#ar" transform="translate(533,530)"/><use href="#ar" transform="translate(778,530)"/><use href="#ar" transform="translate(1020,530)"/>
    <use href="#ar" transform="translate(188,697) rotate(180)"/><use href="#ar" transform="translate(323,697) rotate(180)"/><use href="#ar" transform="translate(540,697) rotate(180)"/><use href="#ar" transform="translate(755,697) rotate(180)"/><use href="#ar" transform="translate(1010,697) rotate(180)"/>
    <use href="#ar" transform="translate(225,872)"/><use href="#ar" transform="translate(462,872)"/><use href="#ar" transform="translate(772,872)"/><use href="#ar" transform="translate(1080,872)"/>
    <use href="#ar" transform="translate(185,1013) rotate(180)"/><use href="#ar" transform="translate(455,1013) rotate(180)"/><use href="#ar" transform="translate(705,1013) rotate(180)"/><use href="#ar" transform="translate(945,1013) rotate(180)"/>
    <use href="#ar" transform="translate(295,1188)"/><use href="#ar" transform="translate(392,1188)"/><use href="#ar" transform="translate(585,1188)"/><use href="#ar" transform="translate(838,1188)"/><use href="#ar" transform="translate(1078,1188)"/>
    <use href="#ar" transform="translate(185,1368) rotate(180)"/><use href="#ar" transform="translate(425,1368) rotate(180)"/><use href="#ar" transform="translate(618,1368) rotate(180)"/><use href="#ar" transform="translate(820,1368) rotate(180)"/><use href="#ar" transform="translate(1055,1368) rotate(180)"/>
  </g>

  <!-- Step nodes -->
  <g class="nodes">
    <g><circle class="node" cx="68" cy="117" r="26"/><use class="glyph" href="#i-phone" x="55" y="104" width="26" height="26"/></g>
    <g><circle class="node" cx="373" cy="200" r="26"/><use class="glyph" href="#i-people" x="360" y="187" width="26" height="26"/></g>
    <g><circle class="node" cx="586" cy="200" r="26"/><use class="glyph" href="#i-card" x="573" y="187" width="26" height="26"/></g>
    <g><circle class="node" cx="769" cy="200" r="26"/><use class="glyph" href="#i-cal" x="756" y="187" width="26" height="26"/></g>
    <g><circle class="node" cx="1083" cy="200" r="26"/><use class="glyph" href="#i-sms" x="1070" y="187" width="26" height="26"/></g>

    <g><circle class="node" cx="115" cy="365" r="26"/><use class="glyph" href="#i-grid" x="102" y="352" width="26" height="26"/></g>
    <g><circle class="node" cx="400" cy="365" r="26"/><use class="glyph" href="#i-clip" x="387" y="352" width="26" height="26"/></g>
    <g><circle class="node" cx="736" cy="365" r="26"/><use class="glyph" href="#i-list" x="723" y="352" width="26" height="26"/></g>
    <g><circle class="node" cx="985" cy="365" r="26"/><use class="glyph" href="#i-order" x="972" y="352" width="26" height="26"/></g>

    <g><circle class="node" cx="68" cy="470" r="26"/><use class="glyph" href="#i-chart" x="55" y="457" width="26" height="26"/></g>
    <g><circle class="node" cx="346" cy="530" r="26"/><use class="glyph" href="#i-book" x="333" y="517" width="26" height="26"/></g>
    <g><circle class="node" cx="696" cy="530" r="26"/><use class="glyph" href="#i-target" x="683" y="517" width="26" height="26"/></g>
    <g><circle class="node" cx="935" cy="530" r="26"/><use class="glyph" href="#i-tick" x="922" y="517" width="26" height="26"/></g>

    <g><circle class="node" cx="114" cy="697" r="26"/><use class="glyph" href="#i-award" x="101" y="684" width="26" height="26"/></g>
    <g><circle class="node" cx="259" cy="697" r="26"/><use class="glyph" href="#i-gift" x="246" y="684" width="26" height="26"/></g>
    <g><circle class="node" cx="475" cy="697" r="26"/><use class="glyph" href="#i-hand" x="462" y="684" width="26" height="26"/></g>
    <g><circle class="node" cx="669" cy="697" r="26"/><use class="glyph" href="#i-doc" x="656" y="684" width="26" height="26"/></g>
    <g><circle class="node" cx="962" cy="697" r="26"/><use class="glyph" href="#i-tag" x="949" y="684" width="26" height="26"/></g>

    <g><circle class="node" cx="116" cy="872" r="26"/><use class="glyph" href="#i-list" x="103" y="859" width="26" height="26"/></g>
    <g><circle class="node" cx="351" cy="872" r="26"/><use class="glyph" href="#i-mail" x="338" y="859" width="26" height="26"/></g>
    <g><circle class="node" cx="620" cy="872" r="26"/><use class="glyph" href="#i-checklist" x="607" y="859" width="26" height="26"/></g>
    <g><circle class="node" cx="936" cy="872" r="26"/><use class="glyph" href="#i-cloud" x="923" y="859" width="26" height="26"/></g>

    <g><circle class="node" cx="139" cy="1013" r="26"/><use class="glyph" href="#i-folder" x="126" y="1000" width="26" height="26"/></g>
    <g><circle class="node" cx="388" cy="1013" r="26"/><use class="glyph" href="#i-network" x="375" y="1000" width="26" height="26"/></g>
    <g><circle class="node" cx="652" cy="1013" r="26"/><use class="glyph" href="#i-add" x="639" y="1000" width="26" height="26"/></g>
    <g><circle class="node" cx="886" cy="1013" r="26"/><use class="glyph" href="#i-save" x="873" y="1000" width="26" height="26"/></g>

    <g><circle class="node" cx="115" cy="1188" r="26"/><use class="glyph" href="#i-invoice" x="102" y="1175" width="26" height="26"/></g>
    <g><circle class="node" cx="462" cy="1188" r="26"/><use class="glyph" href="#i-form" x="449" y="1175" width="26" height="26"/></g>
    <g><circle class="node" cx="700" cy="1188" r="26"/><use class="glyph" href="#i-gavel" x="687" y="1175" width="26" height="26"/></g>
    <g><circle class="node" cx="887" cy="1188" r="26"/><use class="glyph" href="#i-paper" x="874" y="1175" width="26" height="26"/></g>

    <g><circle class="node" cx="114" cy="1368" r="26"/><use class="glyph" href="#i-cal" x="101" y="1355" width="26" height="26"/></g>
    <g><circle class="node" cx="313" cy="1358" r="26"/><use class="glyph" href="#i-plan" x="300" y="1345" width="26" height="26"/></g>
    <g><circle class="node" cx="499" cy="1368" r="26"/><use class="glyph" href="#i-shield" x="486" y="1355" width="26" height="26"/></g>
    <g><circle class="node" cx="701" cy="1368" r="26"/><use class="glyph" href="#i-clock" x="688" y="1355" width="26" height="26"/></g>
    <g><circle class="node" cx="887" cy="1368" r="26"/><use class="glyph" href="#i-box" x="874" y="1355" width="26" height="26"/></g>
  </g>

  <!-- Step descriptions -->
  <g class="steps">
    <text class="step-text" x="105" y="109"><tspan>Agent <tspan class="kw">CALLS</tspan> potential</tspan><tspan x="105" dy="23">client to arrange a time to</tspan><tspan x="105" dy="23">meet and obtain details</tspan><tspan x="105" dy="23">about the property</tspan></text>
    <text class="step-text" x="347" y="106"><tspan>Agent ensures all</tspan><tspan x="347" dy="23">decision makers will be</tspan><tspan x="347" dy="23">present at <tspan class="kw">MEETING</tspan></tspan></text>
    <text class="step-text" x="560" y="106"><tspan>Agent adds vendors</tspan><tspan x="560" dy="23"><tspan class="kw">CONTACT</tspan> details</tspan><tspan x="560" dy="23">on phone</tspan></text>
    <text class="step-text" x="744" y="106"><tspan>Agent adds</tspan><tspan x="744" dy="23">appointment to</tspan><tspan x="744" dy="23">personal <tspan class="kw">CALENDAR</tspan></tspan></text>
    <text class="step-text" x="955" y="109"><tspan>Agent sends <tspan class="kw">SMS</tspan></tspan><tspan x="955" dy="23">to potential client to</tspan><tspan x="955" dy="23">thank them for the</tspan><tspan x="955" dy="23">opportunity</tspan></text>

    <text class="step-text" x="62" y="264"><tspan>Admin/Agent <tspan class="kw">DELIVERS</tspan></tspan><tspan x="62" dy="23">pre-listing kit (preferably</tspan><tspan x="62" dy="23">within the hour) &amp; SMS</tspan><tspan x="62" dy="23">potential vendor</tspan></text>
    <text class="step-text" x="346" y="264"><tspan>Admin prepares pre-listing kit with</tspan><tspan x="346" dy="23"><tspan class="kw">QUESTIONNAIRE</tspan>, sample</tspan><tspan x="346" dy="23">brochure &amp; cover letter, property</tspan><tspan x="346" dy="23">magazine, agent profile booklet</tspan></text>
    <text class="step-text" x="693" y="264"><tspan>Agent completes a TMP</tspan><tspan x="693" dy="23">to provide to Admin for</tspan><tspan x="693" dy="23"><tspan class="kw">PRELISTING</tspan> kit prep</tspan></text>
    <text class="step-text" x="955" y="264"><tspan>Agent/Admin</tspan><tspan x="955" dy="23"><tspan class="kw">ORDERS</tspan> ARE</tspan><tspan x="955" dy="23">from Kellerman's</tspan></text>

    <text class="step-text" x="106" y="422"><tspan>Admin/Agent to</tspan><tspan x="106" dy="23">research &amp; prints</tspan><tspan x="106" dy="23">comparable Sales</tspan><tspan x="106" dy="23" class="kw">REPORTS</tspan></text>
    <text class="step-text" x="321" y="420"><tspan>Admin prepares TMP with</tspan><tspan x="321" dy="23"><tspan class="kw">MARKETING</tspan><tspan font-size="16"> Costs Selection booklet,</tspan></tspan><tspan x="321" dy="21" font-size="16">Service Offering Selection booklet, Sales</tspan><tspan x="321" dy="21" font-size="16">Agency Agreement &amp; Benefits Form, ARE</tspan></text>
    <text class="step-text" x="671" y="422"><tspan>Admin enters potential</tspan><tspan x="671" dy="23">Vendor into CRM &amp; set</tspan><tspan x="671" dy="23">“Appraisal” <tspan class="kw">TRACK</tspan></tspan></text>
    <text class="step-text" x="910" y="422"><tspan>Agent <tspan class="kw">CONFIRMS</tspan></tspan><tspan x="910" dy="23">appraisal on the morning</tspan><tspan x="910" dy="23">of the appointment with</tspan><tspan x="910" dy="23">an SMS</tspan></text>

    <text class="step-text" x="62" y="588"><tspan>Agent meets with</tspan><tspan x="62" dy="23">potential Vendor</tspan><tspan x="62" dy="23">and completes the</tspan><tspan x="62" dy="23" class="kw">APPRAISAL</tspan></text>
    <text class="step-text" x="233" y="586"><tspan>Admin prepares written</tspan><tspan x="233" dy="23">appraisal report</tspan><tspan x="233" dy="23">hand-deliver with coffee</tspan><tspan x="233" dy="23">vouchers &amp;/or <tspan class="kw">GIFT</tspan></tspan></text>
    <text class="step-text" x="450" y="586"><tspan>Agent <tspan class="kw">HAND-</tspan></tspan><tspan x="450" dy="23"><tspan class="kw">DELIVERS</tspan> report</tspan><tspan x="450" dy="23">with coffee voucher</tspan><tspan x="450" dy="23">or Brookes chocolates</tspan></text>
    <text class="step-text" x="643" y="588"><tspan>Agent receives confirmation from</tspan><tspan x="643" dy="23">vendor to proceed with listing &amp;</tspan><tspan x="643" dy="23">arranges signing of Residential</tspan><tspan x="643" dy="23">Sales Agency <tspan class="kw">AGREEMENT</tspan></tspan></text>
    <text class="step-text" x="937" y="586"><tspan>Admin checks</tspan><tspan x="937" dy="23">Residential <tspan class="kw">SALES</tspan></tspan><tspan x="937" dy="23">Agency &amp; enters as</tspan><tspan x="937" dy="23">Listing into CRM</tspan></text>

    <text class="step-text" x="88" y="754"><tspan>Admin completes the</tspan><tspan x="88" dy="23">"New Listing</tspan><tspan x="88" dy="23"><tspan class="kw">CHECKLIST</tspan>" and</tspan><tspan x="88" dy="23">prepares black folder</tspan></text>
    <text class="step-text" x="320" y="754"><tspan>Admin checks for Vendor</tspan><tspan x="320" dy="23"><tspan class="kw">EMAIL</tspan> addresses &amp; if</tspan><tspan x="320" dy="23">required call or SMS</tspan><tspan x="320" dy="23">client to obtain</tspan></text>
    <text class="step-text" x="587" y="754"><tspan>Admin sets track (<tspan class="kw">NEW</tspan></tspan><tspan x="587" dy="23"><tspan class="kw">LISTING 1</tspan>) as at date of signing</tspan><tspan x="587" dy="23">Sales Agency &amp; removes</tspan><tspan x="587" dy="23">Appraisal trail (if applicable)</tspan></text>
    <text class="step-text" x="929" y="754"><tspan>Admin completes</tspan><tspan x="929" dy="23">the marketing</tspan><tspan x="929" dy="23">section of <tspan class="kw">CRM</tspan></tspan></text>

    <text class="step-text" x="101" y="928"><tspan>Admin creates OFI</tspan><tspan x="101" dy="23"><tspan class="kw">FOLDER</tspan> (including rental</tspan><tspan x="101" dy="23">appraisal from ValueTrack)</tspan></text>
    <text class="step-text" x="373" y="928"><tspan>Admin scans &amp; files</tspan><tspan x="373" dy="23">Residential Sales Agency</tspan><tspan x="373" dy="23">in <tspan class="kw">NETWORK</tspan> folder</tspan></text>
    <text class="step-text" x="631" y="928"><tspan>Admin <tspan class="kw">CREATES</tspan></tspan><tspan x="631" dy="23">Property Folder in</tspan><tspan x="631" dy="23">Network</tspan></text>
    <text class="step-text" x="861" y="928"><tspan>Admin confirms if Marketing</tspan><tspan x="861" dy="23">has been paid upfront and</tspan><tspan x="861" dy="23">prints/<tspan class="kw">SAVES</tspan> Tax Invoice</tspan></text>

    <text class="step-text" x="88" y="1073"><tspan>Admin email/post "Thank You For</tspan><tspan x="88" dy="23">Listing" letter with copy of Sales</tspan><tspan x="88" dy="23">Agency Agreement &amp; Seller's</tspan><tspan x="88" dy="23">Guide &amp; Marketing Tax <tspan class="kw">INVOICE</tspan></tspan></text>
    <text class="step-text" x="437" y="1073"><tspan>Admin sends Form 1</tspan><tspan x="437" dy="23">Request Email</tspan><tspan x="437" dy="23">through to</tspan><tspan x="437" dy="23">Kellerman <tspan class="kw">FORMS</tspan></tspan></text>
    <text class="step-text" x="676" y="1073"><tspan>If <tspan class="kw">AUCTION</tspan></tspan><tspan x="676" dy="23">- Agent books</tspan><tspan x="676" dy="23">auctioneer</tspan></text>
    <text class="step-text" x="853" y="1073"><tspan>If Auction - Admin</tspan><tspan x="853" dy="23">completes auction day</tspan><tspan x="853" dy="23">checklist and auction day</tspan><tspan x="853" dy="23"><tspan class="kw">PAPERWORK</tspan> checklist</tspan></text>

    <text class="step-text" x="64" y="1252"><tspan>Agent adds</tspan><tspan x="64" dy="23">appointments to</tspan><tspan x="64" dy="23">personal <tspan class="kw">CALENDAR</tspan></tspan></text>
    <text class="step-text" x="287" y="1249"><tspan>Agent organises</tspan><tspan x="287" dy="23">Home Stylist,</tspan><tspan x="287" dy="23" class="kw">FLOOR PLAN</tspan><tspan x="287" dy="23">&amp; Photography</tspan></text>
    <text class="step-text" x="474" y="1249"><tspan>Admin <tspan class="kw">SECURES</tspan></tspan><tspan x="474" dy="23">keys and stores in</tspan><tspan x="474" dy="23">key safe</tspan></text>
    <text class="step-text" x="675" y="1249"><tspan>Agent to organise a</tspan><tspan x="675" dy="23"><tspan class="kw">TIME</tspan> to have dropped</tspan><tspan x="675" dy="23">off to office or collect</tspan><tspan x="675" dy="23">keys if Vendor agrees</tspan></text>
    <text class="step-text" x="906" y="1249"><tspan>Agent/Admin creates</tspan><tspan x="906" dy="23">and delivers Just</tspan><tspan x="906" dy="23">Listed <tspan class="kw">LETTERBOX</tspan></tspan><tspan x="906" dy="23">drops</tspan></text>
  </g>
</svg>
</body>
</html>
```